Hi Marlow,

I would like you to design for me a menu board for all my products.

The layout I have hand drawn for you so just follow my layout.

Pho
Noodle salads
Rice
StirFry with Thick Rice Noodles
Spring Rolls Ricepaper Rolls

Poster Size: AO Vertical ( 841W x 1189H)

There are more photos of the rice dishes but I thought I can send this through so you can start and I can send you the rest of the photos when I get back from my photographer.

I will have items descriptions to follow also

Requirements
Must have

```html
<!DOCTYPE html>
<html lang="en">
<head>
<meta charset="utf-8">
<title>Menu Board</title>
<link href="https://fonts.googleapis.com/css2?family=Lobster&family=Varela+Round&display=swap" rel="stylesheet">
<style>
  :root {
    --frame-light: #c9a45c;
    --frame-mid: #a9853f;
    --frame-dark: #7d5f28;
    --board-centre: #3b3c3e;
    --board-edge: #141516;
    --title-gold: #8c6a35;
    --title-outline: #ffffff;
    --rule: #e6e6e6;
    --label: #f2f2f2;
    --photo-shadow: rgba(0,0,0,0.55);
  }
  * { box-sizing: border-box; margin: 0; padding: 0; }
  html, body { width: 849px; height: 1200px; overflow: hidden; background: #ffffff; }
  .poster {
    position: relative;
    width: 849px;
    height: 1200px;
    background: linear-gradient(135deg, var(--frame-light) 0%, var(--frame-mid) 45%, var(--frame-dark) 100%);
  }
  .board {
    position: absolute;
    left: 50px;
    top: 64px;
    width: 750px;
    height: 1068px;
    background: radial-gradient(ellipse at 50% 40%, var(--board-centre) 0%, #242527 55%, var(--board-edge) 100%);
    box-shadow: inset 0 0 18px rgba(0,0,0,0.7);
  }
  .board::before {
    content: "";
    position: absolute;
    inset: -6px;
    border: 6px solid var(--frame-dark);
    opacity: 0.55;
    pointer-events: none;
  }
  .menu-title {
    position: absolute;
    left: 0;
    top: 70px;
    width: 849px;
    height: 150px;
  }
  .menu-title text {
    font-family: "Lobster", cursive;
    font-size: 122px;
    fill: var(--title-gold);
    stroke: var(--title-outline);
    stroke-width: 7px;
    paint-order: stroke fill;
    stroke-linejoin: round;
  }
  .menu-row {
    position: absolute;
    display: grid;
  }
  .dish {
    display: flex;
    flex-direction: column;
    align-items: center;
  }
  .dish-photo {
    border-radius: 50%;
    box-shadow: 3px 4px 6px var(--photo-shadow);
  }
  .dish-name {
    width: 100%;
    display: flex;
    align-items: center;
    justify-content: center;
    border: 1.5px solid var(--rule);
    border-left-width: 0;
    color: var(--label);
    font-family: "Varela Round", sans-serif;
    white-space: nowrap;
    letter-spacing: 0.2px;
  }
  .dish:first-child .dish-name { border-left-width: 1.5px; }

  /* Pho row */
  .row-pho { left: 110px; top: 246px; width: 626px; grid-template-columns: repeat(3, 1fr); }
  .row-pho .dish-photo { width: 116px; height: 116px; margin-bottom: 8px; }
  .row-pho .dish-name { height: 46px; font-size: 18px; }

  /* Four-up rows */
  .row-four { left: 110px; width: 626px; grid-template-columns: repeat(4, 1fr); }
  .row-four .dish-photo { width: 80px; height: 80px; }
  .row-four .dish-name { height: 36px; font-size: 12px; }
  .row-salads { top: 436px; }
  .row-salads .dish-photo { margin-bottom: 22px; }
  .row-rice { top: 596px; }
  .row-rice .dish-photo { margin-bottom: 20px; }
  .row-stirfry { top: 754px; }
  .row-stirfry .dish-photo { margin-bottom: 20px; }
  .dish-name.is-long { font-size: 9px; }

  /* Rolls row */
  .row-rolls { left: 214px; top: 914px; width: 418px; grid-template-columns: repeat(2, 1fr); }
  .row-rolls .dish-photo { width: 116px; height: 116px; margin-bottom: 24px; }
  .row-rolls .dish-name { height: 48px; font-size: 18px; }

  /* Photo placeholders */
  .photo-soup { background: radial-gradient(circle at 50% 45%, #6b5a2c 0%, #4e6b2e 40%, #e9e9e6 70%, #ffffff 100%); }
  .photo-soup-tofu { background: radial-gradient(circle at 50% 45%, #c9622f 0%, #9c4a24 40%, #e9e9e6 70%, #ffffff 100%); }
  .photo-salad { background: radial-gradient(circle at 50% 40%, #6d4a2f 0%, #b9a46a 45%, #f2f2f0 75%, #ffffff 100%); }
  .photo-plate-beef { background: radial-gradient(circle at 45% 55%, #7a2e24 0%, #3f7a2e 45%, #f4f4f4 75%, #ffffff 100%); }
  .photo-plate-chicken { background: radial-gradient(circle at 45% 55%, #d9a36a 0%, #3f8a2e 45%, #f4f4f4 75%, #ffffff 100%); }
  .photo-plate-tofu { background: radial-gradient(circle at 45% 55%, #c97a3a 0%, #4a8a30 45%, #f4f4f4 75%, #ffffff 100%); }
  .photo-fried-rice { background: radial-gradient(circle at 50% 50%, #f1d8c4 0%, #e7a98c 45%, #f6efe8 80%, #ffffff 100%); }
  .photo-noodles { background: radial-gradient(circle at 50% 50%, #b8743c 0%, #6e8a3a 45%, #f4f4f4 78%, #ffffff 100%); }
  .photo-spring-rolls { background: radial-gradient(circle at 40% 60%, #b8702e 0%, #d99a55 40%, #f3f3f3 75%, #ffffff 100%); }
  .photo-rice-paper { background: radial-gradient(circle at 45% 55%, #eef2e2 0%, #b9d28c 40%, #c99a63 75%, #3a2e22 100%); }
</style>
</head>
<body>
<main class="poster">
  <div class="board"></div>

  <svg class="menu-title" viewBox="0 0 849 150" aria-label="Menu">
    <text x="424" y="112" text-anchor="middle">Menu</text>
  </svg>

  <section class="menu-row row-pho">
    <div class="dish"><div class="dish-photo photo-soup" role="img" aria-label="Bowl of beef pho with herbs and onion"></div><div class="dish-name">Beef Pho</div></div>
    <div class="dish"><div class="dish-photo photo-soup" role="img" aria-label="Bowl of chicken pho with herbs and onion"></div><div class="dish-name">Chicken Pho</div></div>
    <div class="dish"><div class="dish-photo photo-soup-tofu" role="img" aria-label="Bowl of tofu pho"></div><div class="dish-name">Tofu Pho</div></div>
  </section>

  <section class="menu-row row-four row-salads">
    <div class="dish"><div class="dish-photo photo-salad" role="img" aria-label="Beef noodle salad bowl"></div><div class="dish-name">Beef Noodle salads</div></div>
    <div class="dish"><div class="dish-photo photo-salad" role="img" aria-label="Chicken noodle salad bowl"></div><div class="dish-name">Chicken Noodle salads</div></div>
    <div class="dish"><div class="dish-photo photo-salad" role="img" aria-label="BBQ pork noodle salad bowl"></div><div class="dish-name">BBQ Pork Noodle salads</div></div>
    <div class="dish"><div class="dish-photo photo-salad" role="img" aria-label="Tofu noodle salad bowl"></div><div class="dish-name">Tofu Noodle salads</div></div>
  </section>

  <section class="menu-row row-four row-rice">
    <div class="dish"><div class="dish-photo photo-plate-beef" role="img" aria-label="Plate of beef with vegetables and rice"></div><div class="dish-name">Beef Rice</div></div>
    <div class="dish"><div class="dish-photo photo-plate-chicken" role="img" aria-label="Plate of chicken with vegetables and rice"></div><div class="dish-name">Chicken Rice</div></div>
    <div class="dish"><div class="dish-photo photo-plate-tofu" role="img" aria-label="Plate of tofu with vegetables and rice"></div><div class="dish-name">Tofu Rice</div></div>
    <div class="dish"><div class="dish-photo photo-fried-rice" role="img" aria-label="Plate of fried rice with prawns"></div><div class="dish-name">Fried Rice</div></div>
  </section>

  <section class="menu-row row-four row-stirfry">
    <div class="dish"><div class="dish-photo photo-noodles" role="img" aria-label="Beef stir-fry noodles"></div><div class="dish-name">Beef StirFry Noodles</div></div>
    <div class="dish"><div class="dish-photo photo-noodles" role="img" aria-label="Chicken stir-fry noodles"></div><div class="dish-name is-long">Chicken StirFry Noodles</div></div>
    <div class="dish"><div class="dish-photo photo-noodles" role="img" aria-label="Tofu stir-fry noodles"></div><div class="dish-name">Tofu StirFry Noodles</div></div>
    <div class="dish"><div class="dish-photo photo-fried-rice" role="img" aria-label="Stir-fry with thick rice noodles"></div><div class="dish-name is-long">StirFry with Thick Rice Noodles</div></div>
  </section>

  <section class="menu-row row-rolls">
    <div class="dish"><div class="dish-photo photo-spring-rolls" role="img" aria-label="Fried spring rolls with dipping sauce"></div><div class="dish-name">Spring Rolls</div></div>
    <div class="dish"><div class="dish-photo photo-rice-paper" role="img" aria-label="Fresh rice paper rolls on a board"></div><div class="dish-name">Ricepaper Rolls</div></div>
  </section>
</main>
</body>
</html>
```